Harlowe Wine Label - Design a front and smaller back label for an exclusive red wine

Harlowe Wines produces a very high quality, high priced wine from an old and prestigous vineyard in one of Australia's oldest, but smallest wine growing regions. The grapevines are old (like old men with gnarled arms and trunks) and they produce fewer grapes than younger vines but the grape quality (and thus wine quality) is magnificent and highly sought after as it produces wine of exceptional quality.
The vineyard was purchased by the Harlowe family in February 2010 from a multinational wine company who made wonderful, trophy winning wines for 10 years before the vineyard went into a decline.
The challenge is to produce 2 labels - a simple main front label that focuses on the Harlowe brand and a smaller, information rich, back label that relates the history of the vineyard.
The labels should have a white or charcoal grey background and impart tradition, quality, exclusivity and a little self indulgence which is why we want the family crest incorporated - the choice of font will help.
It might also impart a sense of fun so that it appeals to the 25-35 year old age bracket.
The label should be kept clean and simple not loud and busy. Preferred colours are black, grey and white. Red is fine if used sparingly

Here are the details:_

Front Label (115 long x 65-90mm wide)

Harlowe
Lanternfield Reserve
2011
Mudgee
Wine of Australia 750ml

Back Label (dimensions to suit text and front label design; font size small; text in black so that it is readable in less than optimal light (eg candlelight at a restaurant table).

Harlowe
Lanternfield Reserve 2011

This is the first release of The Lanternfield’s Reserve – just 100 dozen bottles were made. The wine was made from Shiraz and 10% Cabernet Sauvignon grapes sourced from an iconic Mudgee vineyard that was established 1966 by Peter Kell. In 1994, the vineyard known as ”Silverbrook”, became the source of a decade of formidable, trophy winning wines under Ashgrove’s and later Penwick’s ownership. The 20ha vineyard was purchased by Morag & Helen Harlowe in 2010. The Silverbrook name was retained by Penwicks; no wine has been released under this label since the 2006 vintage.

The shaky old Shiraz vines are slowly being restored to full health using careful cane pruning techniques that stimulates fresh, new tissue growth, more even bunch sizes and better grape quality and consistency. The Shiraz grapes used in this wine were hand-picked from two rows of the first crop from the 46 year old, cane pruned vines. The 2011 Reserve is the first step to re-establish the traditions of a famous vineyard and one of Australia’s most sought after export wines.

“Deep and intense purple hues with aromas of ripe blackberry fruits, spice and eucalypt with rich chocolate complemented by subtle oak overtones. A rich and full bodied wine exhibiting a soft yet generous palate with plum, forest fruits and mint chocolate notes. A fine grained tannin structure displaying integrated oak characters adds to the complexity of the wine. This wine was aged for 18 months in a blend of new French oak hogsheads and one year old American hogsheads, crafting a blend with great structure and length of flavour which will develop into a Mudgee classic” – Owen Pratley, Winemaker

13.5% Alc/Vol.
Contains approx 8.0 std drinks
Preservative (220) added

Harlowe Wines
Tallowby Rd, Mudgee 2850
www.harlowewines-example.com.au

Reason: My apologies to the designers who have kindly submitted some wonderful designs. I am trying to achieve a conscentious between shareholders. This is difficult as they are in different parts of the world and I have learned through this experience that opinions on wine labels are quite diverse!!! The feedback I have received so far indicates the following (1) A light or white background is preferred (2) The crest should not be a dominant part of the label (3) The label needs to be clean, fresh and uncomplicated (4) If red is used it should be in minor detail only (5) "Harlowe" should be distinctive. The font is difficult for us! (6) We are considering "The Lanternfield" RESERVE instead of "Lanternfield" RESERVE (7) The text on the back label is too long; I will edit and re-upload Many thanks for your help and patience Kind regards Morag

Good Morning All,
I have edited the back label text to reduce the size of the label. A Word file with the changes has just been uploaded.
Cheers
Morag

Dear Designers,
Thank you all so very much for the wonderful selection of designs you have submitted my family have all been overwhelmed by the quality and skill level exhibited and we all appreciate you your efforts
Kindest regards
Morag

Target Market(s)

25-35 year old men and women of Australia, China, US & UK

Industry/Entity Type

Restaurant

Requirements
Must have
• Crest
Should not have
• Animals on the label

```html
<!DOCTYPE html>
<html lang="en">
<head>
<meta charset="utf-8">
<title>Harlowe – The Lanternfield Reserve 2011</title>
<link rel="stylesheet" href="https://fonts.googleapis.com/css2?family=Montserrat:wght@300;600;700&family=Pinyon+Script&display=swap">
<style>
  :root {
    --label-cream: #fbfbed;
    --ink: #111111;
    --reserve-red: #ee1c1c;
    --artwork-grey: #b9bab2;
    --artwork-light: #dcdcd2;
  }
  html, body {
    margin: 0;
    padding: 0;
    width: 731px;
    height: 1200px;
    overflow: hidden;
    background: var(--label-cream);
  }
  .label {
    position: relative;
    width: 731px;
    height: 1200px;
    background: var(--label-cream);
    color: var(--ink);
    font-family: "Montserrat", sans-serif;
  }
  .label > * {
    position: absolute;
    left: 0;
    width: 100%;
    margin: 0;
    text-align: center;
    line-height: 1;
  }
  .brand-name {
    top: 52px;
    font-size: 64px;
    font-weight: 600;
    letter-spacing: 5px;
    padding-left: 5px;
    box-sizing: border-box;
  }
  .crest-artwork {
    top: 146px;
    left: 209px;
    width: 313px;
    height: 345px;
    background: linear-gradient(180deg, var(--artwork-light) 0%, var(--artwork-grey) 50%, var(--artwork-light) 100%);
  }
  .wine-name {
    top: 648px;
    font-family: "Pinyon Script", cursive;
    font-size: 84px;
    font-weight: 400;
    line-height: 1.2;
  }
  .reserve {
    top: 803px;
    font-size: 56px;
    font-weight: 700;
    letter-spacing: 0;
    color: var(--reserve-red);
  }
  .vintage {
    top: 1011px;
    font-size: 45px;
    font-weight: 700;
  }
  .region {
    top: 1071px;
    font-size: 37px;
    font-weight: 300;
  }
  .origin {
    top: 1114px;
    font-size: 37px;
    font-weight: 300;
  }
</style>
</head>
<body>
  <main class="label">
    <h1 class="brand-name">HARLOWE</h1>
    <div class="crest-artwork" role="img" aria-label="Family crest artwork"></div>
    <h2 class="wine-name">The Lanternfield</h2>
    <p class="reserve">RESERVE</p>
    <p class="vintage">2011</p>
    <p class="region">MUDGEE</p>
    <p class="origin">WINE OF AUSTRALIA</p>
  </main>
</body>
</html>
```